Varolta Business Card

I am looking for a business card design for a start-up company called Varolta Group. This is a management consultancy focused on sales, marketing, sales management, product management and AGILE software development. Our primary customers are $1M to $50M in revenue.

Varolta is the Italian word for "slope."

The path from $0 to $50M has many different growth stages associated with it. Each one having a significant slope to the next plateau. Our expertise helps our customers ascend each of those slopes. We bring experience, successful track-records in growing companies, best practices and a dive-in and roll-up your sleeves mentality. We are not sitting at base camp shouting instructions, we are right there with you, on the climb.

Industry/Entity Type

Business

```html
<!DOCTYPE html>
<html lang="en">
<head>
<meta charset="utf-8">
<title>Varolta Business Card</title>
<link rel="stylesheet" href="https://fonts.googleapis.com/css2?family=Open+Sans:wght@300;400;600;700&display=swap">
<style>
  :root {
    --backdrop: #e9e7e3;
    --card-white: #ffffff;
    --brand-blue: #0c5fa3;
    --brand-blue-deep: #094b84;
    --brand-blue-light: #1a74bd;
    --steel-dark: #3f4348;
    --steel-light: #b9bcc0;
    --ink-grey: #5f6469;
    --ink-dark: #2b2e31;
    --on-blue: #ffffff;
  }
  * { box-sizing: border-box; margin: 0; padding: 0; }
  html, body { width: 1200px; height: 865px; overflow: hidden; }
  body {
    background: var(--backdrop);
    font-family: "Open Sans", Arial, sans-serif;
    display: flex;
    flex-direction: column;
    align-items: center;
    justify-content: center;
    gap: 56px;
  }
  .card {
    position: relative;
    width: 620px;
    height: 354px;
    border-radius: 4px;
    overflow: hidden;
    box-shadow: 0 8px 22px rgba(0,0,0,0.18);
  }

  /* Front */
  .card-front { background: var(--card-white); }
  .front-white { position: absolute; inset: 0 0 auto 0; height: 208px; }
  .divider-band {
    position: absolute; left: 0; right: 0; top: 208px; height: 7px;
    background: linear-gradient(90deg, var(--steel-light), var(--steel-dark) 55%, var(--steel-light));
  }
  .front-blue {
    position: absolute; left: 0; right: 0; top: 215px; bottom: 0;
    background: linear-gradient(135deg, var(--brand-blue-light), var(--brand-blue) 50%, var(--brand-blue-deep));
  }
  .brand {
    position: absolute; left: 38px; top: 62px;
    display: flex; align-items: center; gap: 18px;
  }
  .brand-dot {
    width: 70px; height: 70px; border-radius: 50%;
    background: var(--brand-blue);
  }
  .brand-name {
    font-weight: 300; font-size: 66px; line-height: 1;
    color: var(--ink-grey); letter-spacing: 0.5px;
  }
  .holder {
    position: absolute; right: 34px; top: 34px; text-align: right;
  }
  .holder-name {
    font-weight: 700; font-size: 20px; color: var(--ink-dark); letter-spacing: 0.6px;
  }
  .holder-role {
    font-weight: 400; font-size: 14px; color: var(--ink-grey); margin-top: 2px;
  }
  .address {
    position: absolute; left: 40px; top: 156px;
    display: flex; gap: 10px; align-items: flex-start;
    font-size: 13px; line-height: 1.35; color: var(--ink-dark);
  }
  .address svg { flex: none; margin-top: 3px; }
  .contacts {
    position: absolute; left: 40px; right: 34px; top: 250px;
    display: grid; grid-template-columns: 1fr 1fr; row-gap: 22px; column-gap: 20px;
  }
  .contact {
    display: flex; align-items: center; gap: 10px;
    color: var(--on-blue); font-weight: 600; font-size: 15px; letter-spacing: 0.3px;
  }
  .contact svg { flex: none; }

  /* Back */
  .card-back {
    background: linear-gradient(135deg, var(--brand-blue-light), var(--brand-blue) 50%, var(--brand-blue-deep));
  }
  .back-stripes { position: absolute; inset: 0; }
</style>
</head>
<body>

  <section class="card card-front" aria-label="Business card front">
    <div class="front-white"></div>
    <div class="divider-band"></div>
    <div class="front-blue"></div>

    <div class="brand">
      <span class="brand-dot"></span>
      <span class="brand-name">Varolta</span>
    </div>

    <div class="holder">
      <p class="holder-name">ELENA MARCHETTI</p>
      <p class="holder-role">Managing Director</p>
    </div>

    <div class="address">
      <svg width="12" height="17" viewBox="0 0 12 17" aria-hidden="true">
        <path d="M6 0C2.7 0 0 2.6 0 5.9 0 10.3 6 17 6 17s6-6.7 6-11.1C12 2.6 9.3 0 6 0zm0 8.3A2.4 2.4 0 1 1 6 3.5a2.4 2.4 0 0 1 0 4.8z" fill="var(--ink-dark)"/>
      </svg>
      <p>214, 9th floor, Crest Tower<br>Ridgeway Road NTH</p>
    </div>

    <div class="contacts">
      <p class="contact">
        <svg width="11" height="17" viewBox="0 0 11 17" aria-hidden="true">
          <rect x="0.75" y="0.75" width="9.5" height="15.5" rx="1.5" fill="none" stroke="#fff" stroke-width="1.5"/>
          <circle cx="5.5" cy="13.3" r="1" fill="#fff"/>
        </svg>
        014 552 7310
      </p>
      <p class="contact">
        <svg width="15" height="15" viewBox="0 0 24 24" aria-hidden="true">
          <path d="M6.6 10.8a15.1 15.1 0 0 0 6.6 6.6l2.2-2.2c.3-.3.7-.4 1-.2 1.1.4 2.3.6 3.6.6.6 0 1 .4 1 1V20c0 .6-.4 1-1 1A17 17 0 0 1 3 4c0-.6.4-1 1-1h3.5c.6 0 1 .4 1 1 0 1.3.2 2.5.6 3.6.1.3 0 .7-.2 1z" fill="#fff"/>
        </svg>
        014 552 7310
      </p>
      <p class="contact">
        <svg width="15" height="15" viewBox="0 0 24 24" aria-hidden="true">
          <g fill="none" stroke="#fff" stroke-width="1.8">
            <circle cx="12" cy="12" r="10"/>
            <ellipse cx="12" cy="12" rx="4.5" ry="10"/>
            <path d="M2 12h20M4 6.5h16M4 17.5h16"/>
          </g>
        </svg>
        www.varoltagroup.com
      </p>
      <p class="contact">
        <svg width="16" height="12" viewBox="0 0 16 12" aria-hidden="true">
          <rect width="16" height="12" rx="1" fill="#fff"/>
          <path d="M0.8 1l7.2 5.6L15.2 1" fill="none" stroke="var(--brand-blue)" stroke-width="1.3"/>
        </svg>
        hello@varoltagroup.com
      </p>
    </div>
  </section>

  <section class="card card-back" aria-label="Business card back">
    <svg class="back-stripes" width="620" height="354" viewBox="0 0 620 354" aria-hidden="true">
      <defs>
        <linearGradient id="steel" x1="0" y1="0" x2="1" y2="0">
          <stop offset="0" stop-color="#b9bcc0"/>
          <stop offset="0.5" stop-color="#3f4348"/>
          <stop offset="1" stop-color="#8c9095"/>
        </linearGradient>
      </defs>
      <polygon points="40,0 58,0 0,100 0,69" fill="url(#steel)"/>
      <polygon points="562,354 580,354 620,285 620,254" fill="url(#steel)"/>
    </svg>
  </section>

</body>
</html>
```